Dune Air & Plus business card

I need an awesome, double-sided business card designed with our new logo. I would like the one side black with the colored logo, and the back side is all yours. I'd like to see horizontal and vertical layouts. Get creative! Thank you.

Target Market(s)

HVAC, Heating and Cooling in Phoenix, AZ

Industry/Entity Type

HVAC

Contact Information for Business Card

We need our new logo on the card. Tom Harker, (623) 555-0142, tom@trydunesair.com, www.trydunesair.com, ROC 514273

```html
<!DOCTYPE html>
<html lang="en">
<head>
<meta charset="utf-8">
<title>Dune Air &amp; Plus — Business Card</title>
<link href="https://fonts.googleapis.com/css2?family=Figtree:wght@500;700;800&display=swap" rel="stylesheet">
<style>
  :root {
    --ink: #050708;
    --paper: #ffffff;
    --backdrop: #3e8fb6;
  }
  * { box-sizing: border-box; margin: 0; padding: 0; }
  html, body { width: 762px; height: 1200px; overflow: hidden; }
  body {
    background: var(--backdrop);
    font-family: "Figtree", sans-serif;
    position: relative;
  }
  .card {
    position: absolute;
    top: 311px;
    width: 330px;
    height: 578px;
    overflow: hidden;
    background: var(--paper);
  }
  .card--front { left: 34px; }
  .card--back { left: 398px; }
  .card__band {
    position: absolute;
    left: 0; width: 100%;
    background: var(--ink);
  }
  .card--front .card__band { top: 0; height: 282px; }
  .card--back .card__band { top: 296px; bottom: 0; }
  .brand {
    position: absolute;
    left: 0; width: 100%;
    display: flex; flex-direction: column; align-items: center; gap: 12px;
    font-weight: 800;
    font-size: 29px;
    letter-spacing: 0.5px;
    text-transform: uppercase;
  }
  .brand__dot { width: 34px; height: 34px; border-radius: 50%; }
  .card--front .brand { top: 95px; color: var(--paper); }
  .card--front .brand__dot { background: var(--paper); }
  .card--back .brand { top: 100px; color: var(--ink); }
  .card--back .brand__dot { background: var(--ink); }

  .contact {
    position: absolute;
    left: 47px; top: 380px;
  }
  .contact__rule { width: 131px; height: 2px; background: var(--ink); }
  .contact__name {
    margin-top: 18px;
    font-weight: 700;
    font-size: 31px;
    color: var(--ink);
    letter-spacing: -0.3px;
  }
  .contact__list { list-style: none; margin-top: 8px; }
  .contact__item {
    display: flex; align-items: center; gap: 10px;
    height: 30px;
    font-weight: 500;
    font-size: 19px;
    color: var(--ink);
    white-space: nowrap;
  }
  .contact__icon { width: 18px; height: 18px; flex: none; }
  .website {
    position: absolute;
    left: 0; width: 100%;
    top: 519px;
    text-align: center;
    color: var(--paper);
    font-weight: 500;
    font-size: 12px;
    letter-spacing: 0.6px;
    text-transform: uppercase;
  }
</style>
</head>
<body>

<section class="card card--front" aria-label="Card front">
  <div class="card__band"></div>
  <div class="brand">
    <span class="brand__dot"></span>
    <span>Dune Air &amp; Plus</span>
  </div>
  <div class="contact">
    <div class="contact__rule"></div>
    <h1 class="contact__name">Tom Harker</h1>
    <ul class="contact__list">
      <li class="contact__item">
        <svg class="contact__icon" viewBox="0 0 20 20" aria-hidden="true">
          <circle cx="10" cy="10" r="10" fill="var(--ink)"/>
          <path d="M6.5 5.5 L8.3 5.2 L9.2 7.6 L8.1 8.6 C8.7 10 9.9 11.2 11.3 11.9 L12.4 10.8 L14.8 11.7 L14.5 13.5 C10 14.2 5.8 10 6.5 5.5Z" fill="var(--paper)"/>
        </svg>
        (623) 555-0142
      </li>
      <li class="contact__item">
        <svg class="contact__icon" viewBox="0 0 20 20" aria-hidden="true">
          <circle cx="10" cy="10" r="3.5" fill="none" stroke="var(--ink)" stroke-width="2"/>
          <path d="M13.5 7 V12 C13.5 14.5 17.5 14.5 17.5 10 A7.5 7.5 0 1 0 13 17" fill="none" stroke="var(--ink)" stroke-width="2"/>
        </svg>
        tom@trydunesair.com
      </li>
      <li class="contact__item">
        <svg class="contact__icon" viewBox="0 0 20 20" aria-hidden="true">
          <circle cx="10" cy="10" r="10" fill="var(--ink)"/>
          <path d="M10 4.5 A3.8 3.8 0 0 1 13.8 8.3 C13.8 11 10 15 10 15 C10 15 6.2 11 6.2 8.3 A3.8 3.8 0 0 1 10 4.5Z" fill="var(--paper)"/>
          <circle cx="10" cy="8.3" r="1.5" fill="var(--ink)"/>
        </svg>
        ROC 514273
      </li>
    </ul>
  </div>
</section>

<section class="card card--back" aria-label="Card back">
  <div class="card__band"></div>
  <div class="brand">
    <span class="brand__dot"></span>
    <span>Dune Air &amp; Plus</span>
  </div>
  <p class="website">www.trydunesair.com</p>
</section>

</body>
</html>
```